Icon Gestaltung für die Begriffe Bonität, Integrität und Legitimität
Zielgruppe
siehe www.feinmetall-pilot.ch
Aufgabenstellung
Das Ziel sind drei stimmige Icons die die Begriffe Bonität, Integrität und Legitimität symbolisieren. ZWINGEND: die drei Icons müssen aufeinander abgestimmt sein. Bitte hinsichtlich Design vorab einen Eindruck auf www.feinmetall-pilot.ch verschaffen.

```html
<!DOCTYPE html>
<html lang="de">
<head>
<meta charset="utf-8">
<title>Dienstleistungen – Feinmetall Pilot</title>
<link href="https://fonts.googleapis.com/css2?family=Open+Sans:wght@400;600&family=Raleway:wght@600;700&display=swap" rel="stylesheet">
<style>
  :root {
    --bg-dark: #252525;
    --bg-header: #ffffff;
    --text-light: #ffffff;
    --text-nav: #222222;
    --accent-blue: #4aa3df;
    --accent-gold: #e0a800;
    --divider: #5a5a5a;
    --icon-area: #3c3c3c;
  }
  * { margin: 0; padding: 0; box-sizing: border-box; }
  html, body { width: 1200px; height: 640px; overflow: hidden; }
  body { background: var(--bg-dark); font-family: "Open Sans", Arial, sans-serif; color: var(--text-light); position: relative; }

  .site-header { position: absolute; top: 0; left: 0; width: 1200px; height: 51px; background: var(--bg-header); }
  .main-nav { position: absolute; right: 110px; top: 0; height: 51px; display: flex; align-items: center; gap: 28px; list-style: none; }
  .main-nav li { font-size: 11.5px; font-weight: 400; letter-spacing: 0.2px; color: var(--text-nav); text-transform: uppercase; }
  .main-nav li.is-active { color: var(--accent-blue); }

  .pillar { position: absolute; top: 161px; width: 240px; text-align: center; }
  .pillar-icon { width: 84px; height: 84px; margin: 0 auto; background: var(--icon-area); border-radius: 4px; }
  .pillar-title { font-family: "Raleway", Arial, sans-serif; font-weight: 700; font-size: 20px; line-height: 24px; margin-top: 26px; }
  .pillar-rule { width: 37px; height: 1px; background: var(--divider); margin: 15px auto 0; }

  .service { position: absolute; top: 353px; width: 290px; }
  .service-icon { position: absolute; top: 2px; }
  .service-icon svg { fill: var(--accent-gold); display: block; }
  .service-title { font-family: "Raleway", Arial, sans-serif; font-weight: 700; font-size: 17.5px; line-height: 25px; max-width: 250px; }
  .service-text { font-size: 12.5px; line-height: 20.3px; margin-top: 18px; width: 280px; }
</style>
</head>
<body>
  <header class="site-header">
    <ul class="main-nav">
      <li>Home</li>
      <li>Facts</li>
      <li class="is-active">Dienstleistungen</li>
      <li>Detailinformationen</li>
      <li>Feinmetall Pilot</li>
      <li>Feinmetall Pilot Blog</li>
      <li>Kontakt</li>
    </ul>
  </header>

  <section class="pillar" style="left:115px">
    <div class="pillar-icon" role="img" aria-label="Icon Bonität: weisse Linienzeichnung"></div>
    <h2 class="pillar-title">Bonität</h2>
    <div class="pillar-rule"></div>
  </section>

  <section class="pillar" style="left:465px">
    <div class="pillar-icon" role="img" aria-label="Icon Integrität: weisse Linienzeichnung"></div>
    <h2 class="pillar-title">Integrität</h2>
    <div class="pillar-rule"></div>
  </section>

  <section class="pillar" style="left:815px">
    <div class="pillar-icon" role="img" aria-label="Icon Legitimität: weisse Linienzeichnung"></div>
    <h2 class="pillar-title">Legitimität</h2>
    <div class="pillar-rule"></div>
  </section>

  <article class="service" style="left:124px">
    <div class="service-icon" style="left:-39px">
      <svg width="20" height="22" viewBox="0 0 20 22"><circle cx="10" cy="6" r="5.5"/><path d="M0 22v-4c0-4 3-6 6-6h8c3 0 6 2 6 6v4z"/></svg>
    </div>
    <h3 class="service-title">Corporate Governance und Corporate Responsibility Beratung</h3>
    <p class="service-text">Evaluation ethische Unternehmensinteressen. Implementation Führungsphilosophie. Umfassende Verantwortungsklärung.</p>
  </article>

  <article class="service" style="left:474px">
    <div class="service-icon" style="left:-46px">
      <svg width="32" height="26" viewBox="0 0 32 26" stroke="#252525" stroke-width="1"><path d="M9 1l7 3v7l-7 3-7-3V4z"/><path d="M2 14l7 3v8l-7-3zM9 17l7-3v8l-7 3z"/><path d="M16 14l7 3v8l-7-3zM23 17l7-3v8l-7 3z"/><path d="M16 4l7-3 7 3v7l-7 3-7-3z"/></svg>
    </div>
    <h3 class="service-title">Unternehmensanalyse und -Darstellung, Corporate Responsibility Regelungen</h3>
    <p class="service-text">Umfassende Unternehmensanalyse und -Darstellung für Kommunikationsansprüche. „pilotbuch“ Corporate Governance Report inkl. Bonitäts-, Integritäts- und Legitimitätsrating. Umfassende Verantwortungszuschreibung und -Zuweisung.</p>
  </article>

  <article class="service" style="left:823px">
    <div class="service-icon" style="left:-35px">
      <svg width="10" height="22" viewBox="0 0 10 22"><rect x="2" y="0" width="5" height="5"/><path d="M0 8h7v11h3v3H0v-3h3v-8H0z"/></svg>
    </div>
    <h3 class="service-title">Exkurs Corporate Governance</h3>
    <p class="service-text">Kurzreferate im Rahmen eines Führungsworkshops, VR- oder Geschäftsleitungs-Offsides.</p>
  </article>
</body>
</html>
```